Using attached logo that has been created

Business card with logo that's attached. Maybe with water or the cartoon van in background. Looking for it to not be so plain and not too white.
Information to include;
Dario Whitlock
(555) 208-7713
Info@mossbrookpipeworks.example
www.mossbrookpipeworks.example
License # 5320417
Looking forward to the designs u come up with.
Thank you!
-Teresa
The designer (Brynn), that I would like to work with requested an extension to allow time to create a couple designs for this project.
Target Market(s)
Plumbing
Industry/Entity Type
Plumbing
Contact Information for Business Card
Listed above
Font styles to use
Look and feel

```html
<!DOCTYPE html>
<html lang="en">
<head>
<meta charset="utf-8">
<title>Mossbrook Pipeworks – Business Card</title>
<link rel="stylesheet" href="https://fonts.googleapis.com/css2?family=Montserrat:wght@400;500;600;700&display=swap">
<style>
  :root {
    --stage: #111214;
    --brand-blue: #1a5bb5;
    --brand-gold: #f2b21c;
    --ink: #1d1f22;
    --paper: #ffffff;
    --paper-shade: #eceff2;
    --slate: #33373c;
    --slate-deep: #202326;
    --edge-blue: #1b4f9e;
  }
  * { box-sizing: border-box; margin: 0; padding: 0; }
  html, body {
    width: 1200px; height: 820px; overflow: hidden;
    background: var(--stage);
    font-family: "Montserrat", Arial, sans-serif;
  }
  .stage {
    width: 1200px; height: 820px;
    display: flex; align-items: center; justify-content: center; gap: 40px;
  }
  .card {
    position: relative;
    width: 560px; height: 320px;
    overflow: hidden;
    border-radius: 3px;
    box-shadow: 0 18px 40px rgba(0,0,0,.55);
  }
  /* Front */
  .card--front {
    background: radial-gradient(circle at 30% 40%, var(--paper) 0%, var(--paper) 55%, var(--paper-shade) 100%);
    border-left: 4px solid var(--edge-blue);
    border-bottom: 4px solid var(--edge-blue);
  }
  .front__droplets {
    position: absolute; inset: 0;
    background: linear-gradient(135deg, rgba(220,226,232,.35), rgba(255,255,255,0) 60%, rgba(214,220,226,.35));
  }
  .front__name {
    position: absolute; left: 46px; top: 62px;
    font-size: 24px; font-weight: 600; letter-spacing: .5px;
    color: var(--brand-blue); text-transform: uppercase;
  }
  .front__contacts {
    position: absolute; left: 46px; top: 142px;
    list-style: none; display: flex; flex-direction: column; gap: 6px;
  }
  .contact {
    display: flex; align-items: center; gap: 8px;
    font-size: 13.5px; font-weight: 500; color: var(--ink);
  }
  .contact svg { width: 15px; height: 15px; flex: none; }
  .contact__accent { color: var(--brand-blue); }
  .front__license {
    position: absolute; left: 56px; bottom: 36px;
    font-size: 17px; font-weight: 500; color: var(--brand-blue);
  }
  .front__license span { color: var(--brand-gold); }
  .front__mascot {
    position: absolute; right: 50px; top: 24px;
    width: 146px; height: 206px;
    border-radius: 8px;
    background: linear-gradient(180deg, #2a66c4 0%, #2a66c4 45%, #9c8466 100%);
  }
  .front__brand {
    position: absolute; right: 22px; top: 244px;
    display: flex; align-items: center; gap: 7px;
    font-size: 17px; font-weight: 700; color: var(--brand-blue);
    text-transform: uppercase; white-space: nowrap;
  }
  .brand-dot { width: 11px; height: 11px; border-radius: 50%; background: var(--brand-gold); flex: none; }

  /* Back */
  .card--back {
    background: radial-gradient(circle at 35% 35%, var(--slate) 0%, var(--slate-deep) 100%);
    border-bottom: 6px solid var(--edge-blue);
  }
  .back__brand {
    position: absolute; left: 40px; top: 74px;
    display: flex; align-items: center; gap: 10px;
    font-size: 26px; font-weight: 700; color: var(--brand-blue);
    text-transform: uppercase; line-height: 1.05;
  }
  .back__brand .brand-dot { width: 13px; height: 13px; }
  .back__van {
    position: absolute; right: 12px; bottom: 22px;
    width: 230px; height: 180px;
    border-radius: 14px;
    background: linear-gradient(180deg, #f1f3f5 0%, #d5dadf 100%);
  }
</style>
</head>
<body>
<main class="stage">
  <section class="card card--front" aria-label="Business card front">
    <div class="front__droplets" aria-hidden="true"></div>
    <h1 class="front__name">Dario Whitlock</h1>
    <ul class="front__contacts">
      <li class="contact">
        <svg viewBox="0 0 24 24" fill="none" stroke="#1a5bb5" stroke-width="2.4" stroke-linecap="round" stroke-linejoin="round"><path d="M22 16.9v3a2 2 0 0 1-2.2 2 19.8 19.8 0 0 1-8.6-3.1 19.5 19.5 0 0 1-6-6A19.8 19.8 0 0 1 2.1 4.2 2 2 0 0 1 4.1 2h3a2 2 0 0 1 2 1.7c.1 1 .4 1.9.7 2.8a2 2 0 0 1-.5 2.1L8 9.9a16 16 0 0 0 6 6l1.3-1.3a2 2 0 0 1 2.1-.4c.9.3 1.8.6 2.8.7a2 2 0 0 1 1.7 2z"/></svg>
        (555) 208-7713
      </li>
      <li class="contact">
        <svg viewBox="0 0 24 24"><rect x="2" y="5" width="20" height="14" rx="1.5" fill="#1a5bb5"/><path d="M2.5 6l9.5 7 9.5-7" fill="none" stroke="#fff" stroke-width="1.6"/></svg>
        Info@mossbrookpipeworks.example
      </li>
      <li class="contact">
        <svg viewBox="0 0 24 24" fill="none" stroke="#1a5bb5" stroke-width="2"><circle cx="12" cy="12" r="10"/><path d="M2 12h20M12 2a15 15 0 0 1 0 20M12 2a15 15 0 0 0 0 20"/></svg>
        <span>www.<span class="contact__accent">mossbrookpipeworks</span>.example</span>
      </li>
    </ul>
    <p class="front__license">License <span># 5320417</span></p>
    <div class="front__mascot" role="img" aria-label="Illustrated plumber mascot in a blue shirt holding a pipe wrench and a circular saw"></div>
    <div class="front__brand"><span class="brand-dot" aria-hidden="true"></span>Mossbrook Pipeworks</div>
  </section>

  <section class="card card--back" aria-label="Business card back">
    <div class="back__brand"><span class="brand-dot" aria-hidden="true"></span>Mossbrook<br>Pipeworks</div>
    <div class="back__van" role="img" aria-label="Cartoon plumber waving a wrench from the window of a white service van"></div>
  </section>
</main>
</body>
</html>
```